Would like a website to blog, vlog and post pictures about a upcoming glowtrek road trip in a 1977 kx van.
We will have custom bumper stickers available (by donation or a set amount - unsure) and would like to be able mail these out in the future.
Would like the website to be easy to use, simple. clean with a modern hippie/boho feel.
The travelling van is original green. We have a custom lic plate 'glowtrek'
The stickers are black, white and red.
Our mission:
A Love movement journey to raise the vibration and awareness of Boundless Glow.
We plan to have it painted with washable paint at certain spots along the way. We will ask willing people to make a journal entry of how they glowtrek (spread the love) and I will quote them in my blog or blog.
The picture attached is me, Dorinda after we painted "Breezy" (the van's given name) with friends for a Canada Day celebration.
The road trip is with my boyfriend and our two 13yr olds - a boy and a girl.
However, the road trip in August is just the beginning of what I envision to be a much longer journey...so I would like the website created to hold space for future adventures :)
Happy creating to whomever feels their heart strings pulled to be part of our glowtrek journey!
With Love and Gratitude,
Dorinda (Band of Sunrise:)
Please note:
KX pic is for inspiration only - please do not use it on the site. Thank you.

Industry/Entity Type

Paint

Requirements
Must have
• Opt in for Future Newsletter, blog, vlog, join the movement - permission to get creative ;)
Email: dorinda@glowtrek.example

```html
<!DOCTYPE html>
<html lang="en">
<head>
<meta charset="utf-8">
<title>glowtrek — A Love Movement Journey</title>
<link href="https://fonts.googleapis.com/css2?family=Questrial&family=Open+Sans:wght@400;600&display=swap" rel="stylesheet">
<style>
  :root{
    --black:#000000;
    --red:#e30613;
    --red-dark:#b8141c;
    --footer-red:#e10b0f;
    --ink:#3a3a3a;
    --muted:#8a8a8a;
    --line:#e2e2e2;
    --white:#ffffff;
  }
  *{box-sizing:border-box;margin:0;padding:0}
  html,body{width:867px;height:1200px;overflow:hidden;background:var(--white)}
  body{position:relative;font-family:"Open Sans",Arial,sans-serif;color:var(--ink)}
  .abs{position:absolute}
  .header-band{left:0;top:0;width:867px;height:194px;background:var(--black)}
  .brand{left:109px;top:20px;color:var(--white);font-family:"Questrial",sans-serif;display:flex;align-items:center;gap:8px}
  .brand-mark{width:18px;height:18px;border-radius:50%;background:var(--red);flex:none}
  .brand-name{font-size:32px;letter-spacing:1px;line-height:1}
  .brand-sub{font-size:10px;letter-spacing:1px;margin-top:4px;padding-left:42px}
  .nav{left:343px;top:38px;display:flex;align-items:center;font-family:"Questrial",sans-serif;font-size:11.5px;color:var(--white)}
  .nav a{color:var(--white);text-decoration:none;padding:0 14.5px;line-height:30px}
  .nav a.active{background:var(--red);border-radius:15px;font-weight:600;padding:0 16px}
  .hero{left:104px;top:87px;width:659px;height:307px;border:1px solid var(--line);
    background:
      radial-gradient(circle at 18px 12px,transparent 0,transparent 0),
      linear-gradient(180deg,rgba(0,0,0,0) 0%,rgba(0,0,0,0) 78%,#5d6e3c 88%,#3d4a26 100%),
      radial-gradient(ellipse at 20% 20%,#fdf9ea 0%,#f4eacb 40%,#e9dcb6 70%,#d7c79c 100%)}
  .hero-dots{left:408px;top:374px;display:flex;gap:5px}
  .hero-dots span{width:9px;height:9px;border-radius:50%;background:var(--white)}
  .mission{left:104px;top:421px;width:659px;text-align:center}
  .mission h1{font-family:"Questrial",sans-serif;font-weight:400;font-size:19.5px;line-height:22px;color:#3d3d3d}
  .mission p{font-size:8.4px;line-height:16px;color:var(--muted);margin-top:11px;width:700px;margin-left:-20px}
  .donate{left:381px;top:516px;width:105px;height:27px;background:var(--red-dark);border-radius:2px;color:var(--white);
    font-family:"Questrial",sans-serif;font-size:10.5px;line-height:27px;text-align:center}
  .section-title{font-family:"Questrial",sans-serif;font-size:16px;font-weight:400;color:var(--ink)}
  .section-title.red{color:var(--red)}
  .video-card{width:155px}
  .video-thumb{width:155px;height:91px;border:1px solid var(--line);position:relative}
  .play{position:absolute;left:63px;top:32px}
  .video-card h3{font-family:"Questrial",sans-serif;font-weight:400;font-size:11px;margin-top:9px}
  .video-card p{font-size:7.6px;line-height:13px;color:var(--muted);margin-top:2px}
  .video-card time{display:block;font-size:7.6px;color:#222;line-height:13px}
  .post{left:109px;width:400px;display:flex;gap:7px}
  .post-thumb{width:52px;height:43px;flex:none}
  .post h4{font-size:8.6px;font-weight:400;color:var(--red);line-height:12px;margin-top:-2px}
  .post p{font-size:7.6px;line-height:13px;color:#666;margin-top:4px}
  .gallery{left:539px;top:836px;display:grid;grid-template-columns:repeat(3,68px);grid-auto-rows:49px;column-gap:8px;row-gap:7px}
  .footer{left:0;top:1088px;width:867px;height:112px;background:var(--footer-red);color:var(--white)}
  .footer-nav{left:105px;top:23px;font-family:"Questrial",sans-serif;font-size:10.5px;white-space:nowrap}
  .footer-nav span{margin:0 4px}
  .copyright{left:105px;top:44px;font-size:7.5px}
  .social{left:105px;top:64px;display:flex;gap:7px}
  .social svg{display:block}
  .newsletter{left:586px;top:22px;font-family:"Questrial",sans-serif;font-size:10px}
  .news-input{left:586px;top:41px;width:173px;height:20px;border:1px solid #f07a7c;background:#c8070b;font-size:7.5px;line-height:18px;padding-left:10px}
  .news-input svg{position:absolute;right:8px;top:6px}
</style>
</head>
<body>
  <div class="abs header-band"></div>
  <div class="abs brand">
    <div>
      <div class="brand-name">GLOWTREK</div>
      <div class="brand-sub">glowtrek.example</div>
    </div>
    <span class="brand-mark"></span>
  </div>
  <nav class="abs nav">
    <a class="active">HOME</a><a>ABOUT US</a><a>VIDEOS</a><a>BLOG</a><a>GALLERY</a><a>CONTACT</a>
  </nav>

  <div class="abs hero" role="img" aria-label="Red heart-shaped balloons with notes floating above treetops in a hazy sky"></div>
  <div class="abs hero-dots"><span></span><span></span><span></span><span></span></div>

  <section class="abs mission">
    <h1>A Love movement journey which we are planing to raise the<br>vibration and awareness of Boundless Glow.</h1>
    <p>Etiam est nunc venenatis in tristique eu imperdiet ac nisl Cum sociis natoque penatibus et magnis dis parturient montes nascetur ridiculus mus In iaculis facilisis massa<br>Etiam eu urna Sed porta Suspendisse quam leo molestie sed luctus quis feugiat in pede Fusce tellus Sed metus augue convallis et vehicula ut pulvinar</p>
  </section>
  <div class="abs donate">DONTATE NOW</div>

  <h2 class="abs section-title red" style="left:105px;top:577px">Video Blog</h2>

  <article class="abs video-card" style="left:104px;top:604px">
    <div class="video-thumb" role="img" aria-label="Young traveller with a backpack in an open field" style="background:linear-gradient(180deg,#f2f1ec 0%,#e4e1d8 50%,#c7bba0 66%,#a89c80 100%)">
      <svg class="play" width="26" height="26" viewBox="0 0 26 26"><circle cx="13" cy="13" r="12" fill="#222" stroke="#fff" stroke-width="1.5"/><path d="M10 8l8 5-8 5z" fill="#fff"/></svg>
    </div>
    <h3>Video Tittle here</h3>
    <p>Etiam est nunc venenatis in tristique eu imperdiet ac nisl Cum sociis natoqu</p>
    <time>25 June 2013</time>
  </article>
  <article class="abs video-card" style="left:271px;top:604px">
    <div class="video-thumb" role="img" aria-label="Painted green camper van parked on a street" style="background:linear-gradient(180deg,#a7ad8f 0%,#7b8a62 30%,#4e5f3a 60%,#3a4430 80%,#5a5a52 100%)">
      <svg class="play" width="26" height="26" viewBox="0 0 26 26"><circle cx="13" cy="13" r="12" fill="#222" stroke="#fff" stroke-width="1.5"/><path d="M10 8l8 5-8 5z" fill="#fff"/></svg>
    </div>
    <h3>Video Tittle here</h3>
    <p>Etiam est nunc venenatis in tristique eu imperdiet ac nisl Cum sociis natoqu</p>
    <time>15 June 2013</time>
  </article>
  <article class="abs video-card" style="left:435px;top:604px">
    <div class="video-thumb" role="img" aria-label="Van on a desert road beneath a large rock formation" style="background:linear-gradient(180deg,#7d9bb8 0%,#a5b3bf 22%,#8b7b6b 40%,#7a6a58 65%,#9a8a6a 80%,#6e6658 100%)">
      <svg class="play" width="26" height="26" viewBox="0 0 26 26"><circle cx="13" cy="13" r="12" fill="#222" stroke="#fff" stroke-width="1.5"/><path d="M10 8l8 5-8 5z" fill="#fff"/></svg>
    </div>
    <h3>Video Tittle here</h3>
    <p>Etiam est nunc venenatis in tristique eu imperdiet ac nisl Cum</p>
    <time>11 June 2013</time>
  </article>
  <article class="abs video-card" style="left:601px;top:604px">
    <div class="video-thumb" role="img" aria-label="Hiker with a backpack on a country path" style="background:linear-gradient(90deg,#e9ecee 0%,#cdd6dc 30%,#4d6c92 55%,#8d9aa4 75%,#c8c6b8 100%)">
      <svg class="play" width="26" height="26" viewBox="0 0 26 26"><circle cx="13" cy="13" r="12" fill="#222" stroke="#fff" stroke-width="1.5"/><path d="M10 8l8 5-8 5z" fill="#fff"/></svg>
    </div>
    <h3>Video Tittle here</h3>
    <p>Etiam est nunc venenatis in tristique eu imperdiet ac nisl Cum sociis</p>
    <time>08 June 2013</time>
  </article>

  <h2 class="abs section-title" style="left:108px;top:805px">Recent Blog Post</h2>
  <article class="abs post" style="top:835px">
    <div class="post-thumb" role="img" aria-label="Traveller cheering on a train" style="background:linear-gradient(135deg,#2e2a24 0%,#6a5a44 45%,#c8a878 70%,#3a3228 100%)"></div>
    <div><h4>Etiam est nunc venenatis</h4><p>Vivamus porttitor g purus nisi eleifend libero a tempus libero lectus feugiat felis Morbi diam mauris viverra in gravida eu mattis in ante Morbi eget arcu Morbi porta libero</p></div>
  </article>
  <article class="abs post" style="top:898px">
    <div class="post-thumb" role="img" aria-label="Couple posing near a clock tower" style="background:linear-gradient(90deg,#a9bcd0 0%,#8d8a7a 35%,#b07a5a 60%,#6a8a4a 80%,#9fb0c2 100%)"></div>
    <div><h4>Phasellus felis dolor scelerisque a tempus eget lobortis</h4><p>Vivamus porttitor g purus nisi eleifend libero a tempus libero lectus feugiat felis Morbi diam mauris viverra in gravida eu mattis in ante Morbi eget arcu Morbi porta libero</p></div>
  </article>
  <article class="abs post" style="top:957px">
    <div class="post-thumb" role="img" aria-label="Two friends jumping on a hilltop" style="background:linear-gradient(180deg,#f0ece4 0%,#d8d2c6 45%,#8a7a5e 70%,#4e4436 100%)"></div>
    <div><h4>Morbi magna magna tincidunt</h4><p>Vivamus porttitor g purus nisi eleifend libero a tempus libero lectus feugiat felis Morbi diam mauris viverra in gravida eu mattis in ante Morbi eget arcu Morbi porta libero</p></div>
  </article>

  <h2 class="abs section-title" style="left:539px;top:805px">Photo Gallery</h2>
  <div class="abs gallery">
    <div role="img" aria-label="Tourists reading a map" style="background:linear-gradient(180deg,#c8b7a2 0%,#e8dcc8 45%,#a8805e 75%,#6a5040 100%)"></div>
    <div role="img" aria-label="Traveller overlooking a coastal city" style="background:linear-gradient(180deg,#3f7fc2 0%,#7ab0dc 40%,#d8d0c0 65%,#b8a890 100%)"></div>
    <div role="img" aria-label="Traveller sitting in a city square" style="background:linear-gradient(180deg,#dfe2e6 0%,#b8b4ae 40%,#5a6070 70%,#34384a 100%)"></div>
    <div role="img" aria-label="Woman walking down a rural road" style="background:linear-gradient(180deg,#c2d2a8 0%,#8aa868 40%,#b0865a 70%,#7a5a3a 100%)"></div>
    <div role="img" aria-label="Traveller with suitcase among blossoms" style="background:linear-gradient(180deg,#ecdce6 0%,#c8a8c0 35%,#dcd8d4 60%,#7e7a86 100%)"></div>
    <div role="img" aria-label="Hiker with a large backpack" style="background:linear-gradient(90deg,#d6dfe4 0%,#aeb8c0 40%,#6a5a48 60%,#3e4e5a 100%)"></div>
    <div role="img" aria-label="Friends looking at a phone" style="background:linear-gradient(135deg,#dbe8f0 0%,#a8c4d8 40%,#c05040 60%,#2e5a9c 100%)"></div>
    <div role="img" aria-label="City bus at night with light trails" style="background:linear-gradient(180deg,#2a1e12 0%,#7a5020 35%,#f0b838 55%,#e07020 70%,#3a2410 100%)"></div>
    <div role="img" aria-label="Tourist reading a guidebook" style="background:linear-gradient(180deg,#c8d8e8 0%,#e4dcd0 40%,#b05048 70%,#3a5a8a 100%)"></div>
  </div>

  <footer class="abs footer">
    <div class="abs footer-nav">HOME<span>|</span>ABOUT US<span>|</span>SERVICES<span>|</span>VIDEOS<span>|</span>PHOTO GALLERY<span>|</span>BLOG<span>|</span>CONTACT</div>
    <div class="abs copyright">© 2014 Company Name&nbsp; All right reserved&nbsp; Term of Use</div>
    <div class="abs social">
      <svg width="20" height="20" viewBox="0 0 20 20" aria-label="Email"><circle cx="10" cy="10" r="10" fill="#fff"/><rect x="5" y="6.5" width="10" height="7" fill="none" stroke="#e10b0f" stroke-width="1.3"/><path d="M5 6.5l5 4 5-4" fill="none" stroke="#e10b0f" stroke-width="1.3"/></svg>
      <svg width="20" height="20" viewBox="0 0 20 20" aria-label="Share"><circle cx="10" cy="10" r="10" fill="#fff"/><circle cx="6.5" cy="10" r="1.8" fill="#e10b0f"/><circle cx="13.5" cy="6" r="1.8" fill="#e10b0f"/><circle cx="13.5" cy="14" r="1.8" fill="#e10b0f"/><path d="M6.5 10L13.5 6M6.5 10l7 4" stroke="#e10b0f" stroke-width="1.2"/></svg>
      <svg width="20" height="20" viewBox="0 0 20 20" aria-label="Location"><circle cx="10" cy="10" r="10" fill="#fff"/><path d="M10 15.5s-4-4.3-4-7.2a4 4 0 018 0c0 2.9-4 7.2-4 7.2z" fill="#e10b0f"/><circle cx="10" cy="8.3" r="1.4" fill="#fff"/></svg>
    </div>
    <div class="abs newsletter">NEWSLETTER SUBSCRIBE</div>
    <div class="abs news-input">Email address
      <svg width="5" height="7" viewBox="0 0 5 7"><path d="M0 0l5 3.5L0 7z" fill="#fff"/></svg>
    </div>
  </footer>
</body>
</html>
```